Global Consulting firm needs a Business Card Design (Contest)

We need a business card design for a company with global reach called 'Hollowbrook Group'. Hollowbrook Group is a Trusted Procurement Advisor that consults for Pinnacle 400 and Meridel 900 companies to find cost reductions in their spending. We would like to see designs that communicate fiduciary trust and sense of partnership. The Front should have our logo w/ 'trusted procurement advisor', Employee name and title, company address, email, phone and fax (logo attached "Hollowbrook group final"). The color scheme and basic concept should be consistent with our presentation front page (attached "HBG presentation cover page"). The Back should have our website (www.hwbrookllc.com) and an array of our areas of expertise: office supplies, lab supplies, wireless telecom, MRO and IT (see "lab supplies" file for example).

```html
<!DOCTYPE html>
<html lang="en">
<head>
<meta charset="utf-8">
<title>Hollowbrook Group – Business Card</title>
<link rel="stylesheet" href="https://fonts.googleapis.com/css2?family=Caladea:wght@400;700&family=Open+Sans:wght@600&display=swap">
<style>
  :root {
    --page: #e9e6e1;
    --card: #fbfbfb;
    --ink: #1b1b1b;
    --ink-soft: #5a5a5a;
    --accent: #b9532a;
    --gold: #e8c21a;
    --band: #151515;
    --label: #4b5cae;
  }
  * { box-sizing: border-box; margin: 0; padding: 0; }
  html, body { width: 1200px; height: 1023px; overflow: hidden; }
  body {
    background: var(--page);
    font-family: "Caladea", Georgia, serif;
    color: var(--ink);
    position: relative;
  }
  .card {
    position: absolute;
    top: 357px;
    width: 540px;
    height: 309px;
    background: var(--card);
    border-radius: 4px;
    box-shadow: 0 2px 10px rgba(0,0,0,.18);
    overflow: hidden;
  }
  .card--front { left: 40px; }
  .card--back { left: 620px; }

  .brand { position: absolute; display: flex; align-items: center; gap: 12px; }
  .brand__dot { width: 40px; height: 40px; border-radius: 50%; background: var(--gold); flex: none; }
  .brand__name { font-size: 36px; font-weight: 700; color: var(--ink); line-height: 1; letter-spacing: -.3px; }
  .tagline { position: absolute; font-size: 21px; color: var(--ink-soft); letter-spacing: .3px; }

  .card--front .brand { left: 26px; top: 34px; }
  .card--front .tagline { left: 78px; top: 78px; }
  .front__rule { position: absolute; left: 26px; right: 26px; top: 132px; height: 3px; background: var(--accent); }
  .person { position: absolute; right: 26px; top: 146px; text-align: right; }
  .person__name { font-size: 21px; font-weight: 700; }
  .person__title { font-size: 15px; color: var(--accent); }
  .contact { position: absolute; left: 26px; bottom: 24px; list-style: none; font-size: 16px; color: var(--ink-soft); }
  .contact li { display: flex; align-items: center; gap: 8px; line-height: 24px; }
  .contact svg { width: 14px; height: 14px; fill: var(--accent); }
  .address { position: absolute; right: 26px; bottom: 24px; font-size: 16px; color: var(--ink-soft); text-align: right; line-height: 22px; display: flex; gap: 8px; }
  .address svg { width: 14px; height: 18px; fill: var(--accent); margin-top: 3px; }

  .card--back .brand { left: 70px; top: 26px; }
  .card--back .tagline { left: 122px; top: 70px; }
  .band { position: absolute; left: 0; right: 0; top: 112px; height: 34px; background: var(--band); display: flex; align-items: center; justify-content: center; }
  .band__url { color: var(--gold); font-size: 17px; letter-spacing: 2px; }
  .expertise { position: absolute; left: 18px; right: 18px; bottom: 22px; display: flex; justify-content: space-between; list-style: none; }
  .expertise__item { position: relative; width: 92px; height: 112px; border: 1px solid #b9bde0; border-radius: 6px; overflow: hidden; }
  .expertise__photo { position: absolute; inset: 0; }
  .expertise__label { position: absolute; top: 6px; right: 0; background: var(--label); color: #fff; font-family: "Open Sans", Arial, sans-serif; font-size: 9px; font-weight: 600; padding: 2px 6px; border-radius: 3px 0 0 3px; }
  .photo--office { background: linear-gradient(135deg, #f3c2d6, #8fb6e8); }
  .photo--lab { background: linear-gradient(135deg, #f2f2f4, #b7c6e4); }
  .photo--telecom { background: linear-gradient(135deg, #9cc0e8, #3f6fb2); }
  .photo--mro { background: linear-gradient(135deg, #f4f4f4, #c9c9cc); }
  .photo--shipping { background: linear-gradient(135deg, #e9d6b4, #c9a777); }
</style>
</head>
<body>
  <section class="card card--front" aria-label="Card front">
    <div class="brand"><span class="brand__dot"></span><span class="brand__name">Hollowbrook Group</span></div>
    <p class="tagline">Trusted Procurement Advisor</p>
    <div class="front__rule"></div>
    <div class="person">
      <p class="person__name">Daniel Ashford</p>
      <p class="person__title">Director</p>
    </div>
    <ul class="contact">
      <li><svg viewBox="0 0 16 16"><path d="M3 1l3 3-2 2c1 2 3 4 6 6l2-2 3 3-2 2C7 15 1 9 1 3z"/></svg>(866) 555 - 0142</li>
      <li><svg viewBox="0 0 16 16"><rect x="3" y="1" width="10" height="5"/><rect x="1" y="6" width="14" height="7" rx="1"/></svg>(609) 555 - 0187</li>
      <li><svg viewBox="0 0 16 16"><path d="M1 3h14v10H1z M1 3l7 6 7-6" fill="none" stroke="#b9532a" stroke-width="1.6"/></svg>info@hwbrookllc.com</li>
    </ul>
    <div class="address">
      <svg viewBox="0 0 14 18"><path d="M7 0a7 7 0 0 0-7 7c0 5 7 11 7 11s7-6 7-11a7 7 0 0 0-7-7zm0 10a3 3 0 1 1 0-6 3 3 0 0 1 0 6z"/></svg>
      <p>4100 Brookfield Drive<br>Suite 210, Cedar Vale<br>NJ 08190</p>
    </div>
  </section>

  <section class="card card--back" aria-label="Card back">
    <div class="brand"><span class="brand__dot"></span><span class="brand__name">Hollowbrook Group</span></div>
    <p class="tagline">Trusted Procurement Advisor</p>
    <div class="band"><span class="band__url">www.hwbrookllc.com</span></div>
    <ul class="expertise">
      <li class="expertise__item"><div class="expertise__photo photo--office" role="img" aria-label="Photo of colourful office supplies"></div><span class="expertise__label">Office Supplies</span></li>
      <li class="expertise__item"><div class="expertise__photo photo--lab" role="img" aria-label="Photo of laboratory supplies"></div><span class="expertise__label">Lab Supplies</span></li>
      <li class="expertise__item"><div class="expertise__photo photo--telecom" role="img" aria-label="Photo of a mobile phone over a world map"></div><span class="expertise__label">Wireless Telecom</span></li>
      <li class="expertise__item"><div class="expertise__photo photo--mro" role="img" aria-label="Photo of a maintenance tool"></div><span class="expertise__label">MRO</span></li>
      <li class="expertise__item"><div class="expertise__photo photo--shipping" role="img" aria-label="Photo of shipping parcels and a scanner"></div><span class="expertise__label">Shipping/Postage</span></li>
    </ul>
  </section>
</body>
</html>
```